FH banner

we need a banner design (36"x120" horizontal) that will be displayed on a local high school baseball field. My company ( Orbit Print Co) has been producing signage for the Fern Hollow community since 2009. We would like to communicate that we do more than banners. The final design should include the slogan "Signs Shirts Swag" and our Logo.

Target Market(s)

companies, teams, events, shirt and other marketing items.

Industry/Entity Type

Sign, Print,

Font styles to use
Sans Serif

Requirements
Should not have
• no baseball content.

```html
<!DOCTYPE html>
<html lang="en">
<head>
<meta charset="utf-8">
<title>Orbit Print Co – Field Banner</title>
<link rel="stylesheet" href="https://fonts.googleapis.com/css2?family=Montserrat:ital,wght@0,500;0,700;1,400&display=swap">
<style>
  :root {
    --page-bg: #c8c8c8;
    --ink: #000000;
    --paper: #ffffff;
  }
  html, body {
    margin: 0;
    padding: 0;
    overflow: hidden;
  }
  body {
    width: 909px;
    height: 1200px;
    background: var(--page-bg);
    position: relative;
  }
  .field-banner {
    position: absolute;
    left: 33px;
    top: 474px;
    width: 845px;
    height: 252px;
    display: block;
  }
  .banner-ground { fill: var(--ink); }
  .logo-panel { fill: var(--paper); }
  .brand-name {
    font-family: "Montserrat", sans-serif;
    font-weight: 700;
    fill: var(--ink);
  }
  .slogan-initial,
  .slogan-word {
    font-family: "Montserrat", sans-serif;
    font-weight: 500;
  }
  .solid { fill: var(--paper); }
  .outline {
    fill: none;
    stroke: var(--paper);
    stroke-width: 2.5;
  }
  .tagline-band { fill: var(--paper); }
  .tagline {
    font-family: "Montserrat", sans-serif;
    font-style: italic;
    font-weight: 400;
    fill: var(--ink);
  }
</style>
</head>
<body>
  <svg class="field-banner" viewBox="0 0 1558 465" xmlns="http://www.w3.org/2000/svg" aria-label="Orbit Print Co banner: Signs, Shirts, Swag – We've got you covered">
    <rect class="banner-ground" x="0" y="0" width="1558" height="465"/>
    <polygon class="logo-panel" points="0,0 428,0 595,465 0,465"/>

    <g class="brand-lockup">
      <text class="brand-name" x="60" y="215" font-size="92">ORBIT</text>
      <text class="brand-name" x="60" y="315" font-size="92">PRINT CO</text>
    </g>

    <g class="slogan">
      <text class="slogan-initial outline" x="612" y="300" font-size="420">S</text>
      <text class="slogan-initial solid" x="672" y="350" font-size="420">S</text>

      <text class="slogan-word outline" x="952" y="135" font-size="122">IGNS</text>
      <text class="slogan-word solid" x="940" y="125" font-size="122">IGNS</text>

      <text class="slogan-word outline" x="952" y="260" font-size="122">HIRTS</text>
      <text class="slogan-word solid" x="940" y="250" font-size="122">HIRTS</text>

      <text class="slogan-word outline" x="952" y="375" font-size="122">WAG</text>
      <text class="slogan-word solid" x="940" y="365" font-size="122">WAG</text>
    </g>

    <polygon class="tagline-band" points="912,408 1558,408 1558,450 928,450"/>
    <text class="tagline" x="935" y="443" font-size="38" textLength="570" lengthAdjust="spacingAndGlyphs">WE'VE GOT YOU COVERED</text>
  </svg>
</body>
</html>
```